I want a business letter head designed, one that I can have printed but also one that I can use as an insert for proforma documentation that is printed in house.

Business name : RJ Penfold & Associates
Address: PO Box 738
Tewantin Qld 4587

Type of business: Accounting practice- accounting, taxation, audit, self managed superannuation,

Colour scheme: black and blue - previously designed a business card; however the blue that is one the cards is very washed out and I am not particularly happy with it.

Industry/Entity Type

Business

```html
<!DOCTYPE html>
<html lang="en">
<head>
<meta charset="utf-8">
<title>RJ Penfold &amp; Associates – Letterhead</title>
<link rel="stylesheet" href="https://fonts.googleapis.com/css2?family=Roboto+Slab:wght@300;400;700&display=swap">
<style>
  :root {
    --ink: #111111;
    --brand-blue: #00eefa;
    --paper: #ffffff;
  }
  * { box-sizing: border-box; margin: 0; padding: 0; }
  html, body {
    width: 923px;
    height: 1200px;
    overflow: hidden;
    background: var(--paper);
  }
  .letterhead {
    position: relative;
    width: 923px;
    height: 1200px;
    background: var(--paper);
    font-family: "Roboto Slab", Georgia, serif;
    color: var(--ink);
  }
  .masthead {
    position: absolute;
    top: 76px;
    left: 0;
    width: 100%;
    display: flex;
    justify-content: center;
    align-items: center;
    gap: 18px;
  }
  .masthead__square {
    width: 62px;
    height: 62px;
    background: var(--brand-blue);
  }
  .masthead__name {
    font-weight: 700;
    font-size: 38px;
    line-height: 36px;
    letter-spacing: -0.3px;
  }
  .masthead__name span { display: block; }
  .masthead__name span:first-child { padding-left: 24px; }

  .contact {
    position: absolute;
    left: 30px;
    top: 1068px;
    padding-left: 19px;
    border-left: 3px solid var(--ink);
    font-size: 15px;
    line-height: 26px;
  }
  .contact__row { display: flex; gap: 8px; }
  .contact__label {
    color: var(--brand-blue);
    font-weight: 700;
    width: 18px;
  }
  .contact__value { font-weight: 400; }

  .services {
    position: absolute;
    right: 34px;
    top: 1060px;
    padding-right: 14px;
    border-right: 3px solid var(--ink);
    text-align: right;
    font-size: 18px;
    line-height: 23px;
  }
  .services__title { font-weight: 700; margin-bottom: 2px; }
  .services__list { list-style: none; font-weight: 300; }
  .services__item::before {
    content: "•";
    color: var(--brand-blue);
    margin-right: 5px;
    font-size: 13px;
  }
  .services__item--inline { display: inline; margin-left: 10px; }
</style>
</head>
<body>
  <main class="letterhead">
    <header class="masthead">
      <div class="masthead__square"></div>
      <h1 class="masthead__name"><span>RJ Penfold</span><span>&amp; Associates.</span></h1>
    </header>

    <footer>
      <address class="contact">
        <div class="contact__row"><span class="contact__label">M:</span><span class="contact__value">0438217604</span></div>
        <div class="contact__row"><span class="contact__label">E:</span><span class="contact__value">rebecca@rjpenfoldassociates.com.au</span></div>
        <div class="contact__row"><span class="contact__label">A:</span><span class="contact__value">PO Box 738, Tewantin Qld 4587</span></div>
      </address>

      <section class="services">
        <h2 class="services__title" style="font-size:18px">Type of Business</h2>
        <ul class="services__list">
          <li class="services__item">Accounting Practice- Accounting</li>
          <li><span class="services__item">Taxation</span><span class="services__item services__item--inline">Audit</span></li>
          <li class="services__item">Self Managed Superannuation</li>
        </ul>
      </section>
    </footer>
  </main>
</body>
</html>
```